Toddler Music Class Bussiness Needs Web Design

We are a small start up called "WeeBopplings" providing music classes to kids from 6 months to 3 years of age. Kids are instructor led and learn to play a variety of instruments (e.g. drums, tambourines, ukulele's, castanets, etc..), develop coordination and rhythm, and stimulate mental development while having a blast of a time along with other kids and their parents.
The website design needs to be clever, have clean lines, simple modern font, original, fun and colourful and professional. It will need to look good when viewed across different devices and be able to scale well when resized.
This website needs to convey the message that the classes will be enjoyed by parents and children, be safe and contribute to the development of their children.
We have a logo that needs to be incorporated into the design and lead the approach. There will be a number of web pages illustrated in the site map accompanied with this project. The winning bid will have a design that represents a number of pages of the website e.g. 4/5 of the pages

****** commercial in confidence ******
Updates

Reason: Hi Designers, appreciate the design submissions thus far. We have decided to extend tge deadline due to requests from designers :)

Just wanted to say thanks for the designs sent through, there are a few good ones (:

In general we are looking for a little more of a playful approach and have included a few variations on the logos to encourage different design approaches.

Feel free to have a play!!

Target Market(s)

Parents in Australia (multicultural) aged 25 to 45

Industry/Entity Type

Learn

Requirements
Must have
• The website design needs to be clever, have clean lines, simple modern font, original, fun and colourful and professional. It will need to look good when viewed across different devices and be able to scale well when resized.
We have a logo that needs to be incorporated into the design and lead the approach.

```html
<!DOCTYPE html>
<html lang="en">
<head>
<meta charset="utf-8">
<title>WeeBopplings – Music classes for little ones</title>
<link href="https://fonts.googleapis.com/css2?family=Ubuntu:wght@400;500;700&family=Arimo:wght@400&display=swap" rel="stylesheet">
<style>
  :root{
    --sky-top:#c7ebfb;
    --sky-bottom:#e6f6fd;
    --page:#ffffff;
    --edge:#9fdcf2;
    --brand-blue:#0a6fbf;
    --brand-purple:#8b3f9e;
    --nav-red:#e5202e;
    --nav-orange:#f7941d;
    --nav-green:#2db34a;
    --nav-coral:#f26a4a;
    --accent-cyan:#1ba1e2;
    --lime:#c8d922;
    --lime-text:#bccd1d;
    --olive:#7f8e12;
    --ink:#1c1c1c;
    --muted:#8a8a8a;
    --footer:#e9eef0;
    --footer-ink:#4a4a4a;
  }
  *{box-sizing:border-box;margin:0;padding:0}
  html,body{width:1053px;height:1200px;overflow:hidden}
  body{
    background:linear-gradient(180deg,var(--sky-top),var(--sky-bottom) 45%,#eef9fe);
    font-family:"Arimo",Arial,sans-serif;color:var(--ink);position:relative;
  }
  .page{position:absolute;left:110px;top:0;width:838px;height:1200px;background:var(--page);
    border-left:1px solid var(--edge);border-right:1px solid var(--edge)}
  .abs{position:absolute}
  .brand{left:11px;top:88px;display:flex;align-items:center;gap:8px;
    font-family:"Ubuntu",sans-serif;font-weight:700;font-size:31px;color:var(--brand-blue)}
  .brand-dot{width:26px;height:26px;border-radius:50%;background:var(--brand-purple)}
  .tagline{left:28px;top:193px;font-family:"Ubuntu",sans-serif;font-size:16.5px;line-height:21px;color:var(--brand-blue)}
  .hero-art{left:283px;top:9px;width:539px;height:293px;border-radius:50% 50% 8px 8px/30% 30% 8px 8px;
    background:linear-gradient(180deg,#eaf6fd 0%,#fbe6c2 40%,#9fd4f4 75%,#2e8fd8 100%)}
  .nav{left:38px;top:328px;display:flex;gap:8px}
  .nav a{display:block;height:42px;line-height:42px;text-align:center;color:#fff;text-decoration:none;
    font-family:"Ubuntu",sans-serif;font-size:17.5px;border-radius:2px;box-shadow:0 1px 2px rgba(0,0,0,.15)}
  .swing{left:19px;top:483px;width:74px;height:91px;background:linear-gradient(180deg,#d8effb,#bfe4f8);border-radius:4px;opacity:.7}
  .slide-art{left:762px;top:531px;width:43px;height:43px;background:linear-gradient(180deg,#eef5c4,#d9e87a);border-radius:4px;opacity:.7}
  .slider{left:91px;top:397px;width:466px;height:213px;background:#f4f4f2;border:1px solid #dcdcdc;box-shadow:0 2px 5px rgba(0,0,0,.15)}
  .slider-photo{left:6px;top:8px;width:457px;height:175px;background:linear-gradient(90deg,#d9c9b2,#c04a3c 35%,#6f8a3c 65%,#c8b59a)}
  .pager{right:10px;bottom:10px;font-family:"Ubuntu",sans-serif;font-size:10px;color:var(--accent-cyan);letter-spacing:3px}
  .pager b{color:#f7941d;font-weight:400}
  .programs{left:556px;top:399px;width:210px;height:211px;background:#fafafa;border:1px solid #dfe9b0}
  .programs h3{position:absolute;left:38px;top:12px;font-family:"Ubuntu",sans-serif;font-weight:500;font-size:14px;color:var(--accent-cyan)}
  .programs .rule{position:absolute;left:10px;top:32px;width:150px;border-top:1px dotted #bbb}
  .prog{position:absolute;left:8px;width:160px}
  .prog h4{font-family:"Ubuntu",sans-serif;font-weight:400;font-size:12.5px;color:var(--lime-text)}
  .prog p{font-size:10px;line-height:12px;color:var(--muted);margin-top:3px}
  .arrow-btn{position:absolute;left:180px;width:24px;height:24px}
  .side-rule{position:absolute;left:166px;top:6px;height:198px;border-left:1px solid #e4ecc0}
  h2{font-family:"Ubuntu",sans-serif;font-weight:500;font-size:22.5px}
  .about{left:36px;top:644px;width:490px}
  .about h2{color:var(--accent-cyan)}
  .about p{margin-top:8px;font-size:11.5px;line-height:15.6px}
  .more{display:flex;align-items:center;gap:6px;font-family:"Ubuntu",sans-serif;font-weight:700;font-size:10px;margin-top:7px}
  .about .more{color:var(--accent-cyan)}
  .hours{left:563px;top:644px;width:200px}
  .hours h2{color:var(--lime-text)}
  .hrow{display:flex;gap:12px;align-items:center;margin-top:10px}
  .hrow small{display:block;font-size:11px;color:var(--muted)}
  .hrow strong{display:block;font-weight:400;font-size:13.5px;margin-top:3px}
  .hdiv{border-top:1px dotted #bbb;margin-top:8px;width:156px;margin-left:48px}
  .band{left:0;top:811px;width:836px;height:337px;background:var(--lime)}
  .feature{position:absolute;top:37px;width:235px;color:#fff}
  .feature h3{font-family:"Ubuntu",sans-serif;font-weight:400;font-size:16px}
  .feature .sub{font-size:11.5px;color:var(--olive);margin:3px 0 0 3px}
  .feature .pic{margin-top:8px;height:101px;background:linear-gradient(90deg,#e9c9a0,#c33a52 45%,#6d2a8e 70%,#2f8fb0)}
  .feature p{margin-top:14px;font-size:11.5px;line-height:15.6px}
  .feature .more{color:var(--olive);margin:9px 0 0 3px}
  .footer{left:0;top:1148px;width:836px;height:52px;background:var(--footer)}
  .footer .copy{position:absolute;left:55px;top:19px;font-size:11px;color:var(--footer-ink)}
  .footer nav{position:absolute;left:270px;top:19px;display:flex;gap:15px;font-size:11px;color:var(--footer-ink)}
  .footer .legal{position:absolute;left:690px;top:17px;font-size:11px;color:var(--footer-ink)}
</style>
</head>
<body>
<div class="page">
  <div class="abs brand"><span class="brand-dot"></span>WeeBopplings</div>
  <p class="abs tagline">Music classes to kids from<br>6 months to 3 years of age.</p>
  <div class="abs hero-art" role="img" aria-label="Illustration of happy children dancing on top of the globe under musical notes"></div>

  <nav class="abs nav">
    <a href="#" style="width:88px;background:var(--brand-purple)">HOME</a>
    <a href="#" style="width:113px;background:var(--brand-blue)">ABOUT US</a>
    <a href="#" style="width:113px;background:var(--nav-red)">CLASSES</a>
    <a href="#" style="width:100px;background:var(--nav-orange)">ENTROL</a>
    <a href="#" style="width:140px;background:var(--nav-green)">CONTACT US</a>
    <a href="#" style="width:157px;background:var(--nav-coral)">MERCHANDISE</a>
  </nav>

  <div class="abs swing" role="img" aria-label="Sketch of a playground swing"></div>
  <div class="abs slide-art" role="img" aria-label="Sketch of a playground slide"></div>

  <div class="abs slider">
    <div class="abs slider-photo" role="img" aria-label="Photo of toddlers playing xylophones in a classroom"></div>
    <div class="abs pager">« 1 2 3 <b>4</b> 5 6 »</div>
  </div>

  <aside class="abs programs">
    <h3>Our Programs</h3>
    <div class="rule"></div>
    <div class="side-rule"></div>
    <div class="prog" style="top:50px"><h4>Loream ipusum title</h4><p>dolor sit amet, consectetur<br>adipisicing elit, sed do eiusmod</p></div>
    <div class="prog" style="top:104px"><h4>Loream ipusum title</h4><p>dolor sit amet, consectetur<br>adipisicing elit, sed do eiusmod</p></div>
    <div class="prog" style="top:158px"><h4>Loream ipusum title</h4><p>dolor sit amet, consectetur<br>adipisicing elit, sed do eiusmod</p></div>
    <svg class="arrow-btn" style="top:10px" viewBox="0 0 24 24"><circle cx="12" cy="12" r="11" fill="none" stroke="var(--lime-text)" stroke-width="1.5"/><path d="M7 12l5-5 5 5M7 17l5-5 5 5" fill="none" stroke="var(--lime-text)" stroke-width="1.5"/></svg>
    <svg class="arrow-btn" style="top:178px" viewBox="0 0 24 24"><circle cx="12" cy="12" r="11" fill="none" stroke="var(--lime-text)" stroke-width="1.5"/><path d="M7 7l5 5 5-5M7 12l5 5 5-5" fill="none" stroke="var(--lime-text)" stroke-width="1.5"/></svg>
  </aside>

  <section class="abs about">
    <h2>About Us</h2>
    <p>Lorem ipsum dolor sit amet, consectetur adipisicing elit, sed do eiusmod tempor incididunt ut labore et dolore magna aliqua. Ut enim ad minim veniam, quis nostrud exercitation ullamco laboris nisi ut aliquip ex ea commodo consequat. Duis aute irure dolor in reprehenderit in voluptate velit esse cillum dolore eu fugiat nulla pariatur.</p>
    <a class="more">READ MORE
      <svg width="26" height="26" viewBox="0 0 26 26"><circle cx="13" cy="13" r="11.5" fill="none" stroke="var(--accent-cyan)" stroke-width="1.5"/><path d="M9 10l3 3-3 3M13 10l3 3-3 3" fill="none" stroke="var(--accent-cyan)" stroke-width="1.4"/></svg></a>
  </section>

  <section class="abs hours">
    <h2>Working Hours</h2>
    <div class="hrow">
      <svg width="36" height="36" viewBox="0 0 36 36"><circle cx="18" cy="18" r="16" fill="none" stroke="var(--lime-text)" stroke-width="2"/><path d="M18 8v10l-6 5" fill="none" stroke="var(--lime-text)" stroke-width="2"/></svg>
      <div><small>7 days weekly</small><strong>10 am - 10 pm</strong></div>
    </div>
    <div class="hdiv"></div>
    <div class="hrow">
      <svg width="36" height="36" viewBox="0 0 36 36"><path d="M4 12c0-5 28-5 28 0v3h-7v-3H11v3H4z" fill="none" stroke="var(--lime-text)" stroke-width="2"/><path d="M9 17h18l3 14H6z" fill="none" stroke="var(--lime-text)" stroke-width="2"/><circle cx="18" cy="24" r="3.5" fill="none" stroke="var(--lime-text)" stroke-width="2"/></svg>
      <div><small>contact us</small><strong>+123 555-010-20</strong></div>
    </div>
  </section>

  <section class="abs band">
    <svg class="abs" style="left:0;top:0" width="836" height="9"><defs><pattern id="teeth" width="14" height="9" patternUnits="userSpaceOnUse"><path d="M0 0L7 9L14 0Z" fill="#fff"/></pattern></defs><rect width="836" height="9" fill="url(#teeth)"/></svg>
    <article class="feature" style="left:36px">
      <h3>What we do</h3><div class="sub">loream ipsum dolar sit amet</div>
      <div class="pic" role="img" aria-label="Photo of a teacher and young girls playing a guitar"></div>
      <p>Lorem ipsum dolor sit amet, consectetur adipisicing elit, sed do eiusmod tempor incidi ut labore et dolore magna aliqua. Ut enim ad minim veniam, quis nostrud exercitation ulla laboris nisi ut aliquip ex ea commodo conse Duis aute irure dolor in reprehenderit in volu.</p>
      <a class="more">READ MORE <svg width="24" height="24" viewBox="0 0 24 24"><circle cx="12" cy="12" r="10.5" fill="#fff" stroke="#fff"/><path d="M8 9l3 3-3 3M12 9l3 3-3 3" fill="none" stroke="var(--lime)" stroke-width="1.5"/></svg></a>
    </article>
    <article class="feature" style="left:305px">
      <h3>Our Services</h3><div class="sub">loream ipsum dolar sit amet</div>
      <div class="pic" role="img" aria-label="Photo of a teacher and young girls playing a guitar"></div>
      <p>Lorem ipsum dolor sit amet, consectetur adipisicing elit, sed do eiusmod tempor incidi ut labore et dolore magna aliqua. Ut enim ad minim veniam, quis nostrud exercitation ulla laboris nisi ut aliquip ex ea commodo conse Duis aute irure dolor in reprehenderit in volu.</p>
      <a class="more">READ MORE <svg width="24" height="24" viewBox="0 0 24 24"><circle cx="12" cy="12" r="10.5" fill="#fff" stroke="#fff"/><path d="M8 9l3 3-3 3M12 9l3 3-3 3" fill="none" stroke="var(--lime)" stroke-width="1.5"/></svg></a>
    </article>
    <article class="feature" style="left:569px">
      <h3>Active learning</h3><div class="sub">loream ipsum dolar sit amet</div>
      <div class="pic" role="img" aria-label="Photo of a teacher and young girls playing a guitar"></div>
      <p>Lorem ipsum dolor sit amet, consectetur adipisicing elit, sed do eiusmod tempor incidi ut labore et dolore magna aliqua. Ut enim ad minim veniam, quis nostrud exercitation ulla laboris nisi ut aliquip ex ea commodo conse Duis aute irure dolor in reprehenderit in volu.</p>
      <a class="more">READ MORE <svg width="24" height="24" viewBox="0 0 24 24"><circle cx="12" cy="12" r="10.5" fill="#fff" stroke="#fff"/><path d="M8 9l3 3-3 3M12 9l3 3-3 3" fill="none" stroke="var(--lime)" stroke-width="1.5"/></svg></a>
    </article>
  </section>

  <footer class="abs footer">
    <svg class="abs" style="left:0;top:0" width="836" height="8"><defs><pattern id="teeth2" width="14" height="8" patternUnits="userSpaceOnUse"><path d="M0 0L7 8L14 0Z" fill="var(--lime)"/></pattern></defs><rect width="836" height="8" fill="url(#teeth2)"/></svg>
    <span class="copy">©2014 companyname</span>
    <nav><span>Home</span><span>About us</span><span>Classes</span><span>Entrol</span><span>Contact us</span><span>Merchandise</span></nav>
    <span class="legal">Sitemap | Copyrights</span>
  </footer>
</div>
</body>
</html>
```